my catalog design project for KRV tradeshow

We need a catalog design for our ranch equipment manufacturing company. The final design should communicate low cost alternative without compromising quality.
We need all the main product lines show cased in catalog including gates, panels, feeders, cattle squeezes, horse stalls, dog kennels, tractor attachments
The layout, design and colors can reflect the design of the website:

We just need a basic product catalog that uses a similar layout, design, and colors as our website: quillbarnfabricating.com

Catalog should be approximately 6-10 pages long 8.5"x11" first page cover, next inside page company info, then product pages with item picture and description as in the website. For sample submissions, i'd like to see cover page, inside page and a product page.

FOR THE INITIAL ENTRIES, I'm expecting to see
- the cover page,
- inside company info page
- and one product page.

Target Market(s)

Chain Store buyers

Industry/Entity Type

Agriculture

Requirements
Must have
• All the product info details of main products

```html
<!DOCTYPE html>
<html lang="en">
<head>
<meta charset="utf-8">
<title>Quillbarn Fabricating – Company Profile</title>
<link rel="stylesheet" href="https://fonts.googleapis.com/css2?family=Didact+Gothic&display=swap">
<style>
  :root {
    --paper: #f4f4f4;
    --sweep-shadow: #d9d9d9;
    --sweep-mid: #e8e8e8;
    --ink: #111111;
    --accent: #d0111b;
  }
  html, body {
    margin: 0;
    padding: 0;
    overflow: hidden;
    background: #ffffff;
  }
  .page {
    position: relative;
    width: 927px;
    height: 1200px;
    overflow: hidden;
    background: var(--paper);
    font-family: "Didact Gothic", "Century Gothic", sans-serif;
    color: var(--ink);
  }
  .backdrop {
    position: absolute;
    inset: 0;
    width: 927px;
    height: 1200px;
  }
  .brand {
    position: absolute;
    left: 64px;
    top: 78px;
    display: flex;
    align-items: center;
    gap: 10px;
    font-size: 30px;
    letter-spacing: 1px;
    color: var(--ink);
  }
  .brand-dot {
    width: 26px;
    height: 26px;
    border-radius: 50%;
    background: var(--accent);
  }
  .title {
    position: absolute;
    top: 256px;
    left: 0;
    width: 927px;
    text-align: center;
    margin: 0;
    font-weight: 400;
  }
  .title-main {
    display: block;
    font-size: 41px;
    line-height: 42px;
    letter-spacing: 0.5px;
    color: var(--ink);
  }
  .title-sub {
    display: block;
    font-size: 25px;
    line-height: 28px;
    letter-spacing: 0.5px;
    color: var(--accent);
  }
  .profile {
    position: absolute;
    top: 362px;
    left: 40px;
    width: 847px;
    text-align: center;
    text-transform: uppercase;
    font-size: 14.6px;
    line-height: 28.4px;
    letter-spacing: 0.2px;
  }
  .profile p {
    margin: 0 0 28px;
  }
</style>
</head>
<body>
<div class="page">
  <svg class="backdrop" viewBox="0 0 927 1200" aria-hidden="true">
    <defs>
      <linearGradient id="top-shade" x1="0" y1="0" x2="1" y2="1">
        <stop offset="0" stop-color="#e6e6e6"/>
        <stop offset="0.5" stop-color="#d4d4d4"/>
        <stop offset="1" stop-color="#e2e2e2"/>
      </linearGradient>
      <radialGradient id="sheet" cx="0.5" cy="0.45" r="0.7">
        <stop offset="0" stop-color="#ffffff"/>
        <stop offset="0.7" stop-color="#f7f7f7"/>
        <stop offset="1" stop-color="#ededed"/>
      </radialGradient>
    </defs>
    <rect width="927" height="1200" fill="url(#top-shade)"/>
    <path d="M0 0 L400 0 C300 90 150 150 0 150 Z" fill="#f2f2f2" opacity="0.7"/>
    <path d="M600 0 L927 0 L927 120 C820 60 720 30 600 0 Z" fill="#efefef" opacity="0.6"/>
    <path d="M0 330 C160 150 420 60 760 40 C840 35 900 38 927 40 L927 1200 L0 1200 Z" fill="url(#sheet)"/>
    <path d="M0 330 C160 150 420 60 760 40 C840 35 900 38 927 40" fill="none" stroke="#ffffff" stroke-width="3"/>
  </svg>

  <div class="brand">
    <span class="brand-name">QUILL BARN</span>
    <span class="brand-dot"></span>
  </div>

  <h1 class="title">
    <span class="title-main">QUILLBARN</span>
    <span class="title-sub">FABRICATING</span>
  </h1>

  <div class="profile">
    <p>Quill Barn couples a low cost structure with a corporate culture that is driven by attention to detail, innovation, and quality which allows us to offer maximum value to retailers that are looking to increase margins and market share. At Quill Barn we stand behind what we manufacture and our entire management team and workforce is incentivised on quality performance so everybody has a vested interest in the end consumer being completely satisfied.</p>
    <p>Growing up on an acreage and hobby farm, Daniel Harlow (co-founder) had an early appreciation for dependable ranch equipment at an affordable price. Shortly after graduating from business school in 2001, Daniel along with long time family friend, Liam Chen, identified Liam’s home town of Nanjing, China as the ideal place to develop a line of quality livestock equipment. Quill Barn was born out of need for more economically priced livestock handling equipment in 2003.</p>
    <p>In late 2006, we developed a private label line for several of the largest Canadian co-operatives and the product line continues to drive profit growth and market share for these organizations.</p>
    <p>In January of 2008, our factory’s 65,000 square foot roof completely collapsed under the worst snow fall that central China has experienced in over 50 years. The entire workforce and management pitched in to remove the debris and salvage equipment over the Chinese New Year holiday. Once the roof was rebuilt several months later the workforce grew to 80 plus workers, which required an enhancement of our quality control systems. Our team designed and implemented a simple yet effective quality control system in a country that is dominated by piece rate pay. In conjunction with managers and QC engineers, workers downstream in production who identify quality problems receive a piece rate bonus which in turn is deducted from the worker who caused the problem. This system combined with intensive training for new workers and a full time quality control engineer has made our workers very accountable and reduced our quality problems to negligible levels.</p>
  </div>
</div>
</body>
</html>
```